Minimalist Planner/Journal Design

We need a planner/journal designed for daily use in a small group. I've attached a requirements document that outlines what every page needs to have on it. I've also attached a basic rough draft that we had made in Canva but the draft needs to be redesigned to look more in line with the style we need. I've attached some sample pages from some planners we like the style of. Feel free to add your own creativity and stylistic choices but keep in mind we are trying to get a very 'clean and minimalist design'. The deliverables should be both a pdf of the 8 planner pages, as well as the photoshop/gimp/illustrator files for the project.

Font styles to use
Other font styles liked:
• You choose, but we prefer thin , basic/minimal font faces

Requirements
Must have
• Minimal Design

```html
<!DOCTYPE html>
<html lang="en">
<head>
<meta charset="utf-8">
<title>Minimal Planner Pages</title>
<link rel="stylesheet" href="https://fonts.googleapis.com/css2?family=Arvo&display=swap">
<style>
  :root {
    --canvas: #e8e9ea;
    --paper: #ffffff;
    --sage: #e4ebd8;
    --ink: #5a5d58;
    --rule: #9a9c98;
    --grid: #b4b6b2;
  }
  html, body { margin: 0; padding: 0; overflow: hidden; background: var(--canvas); }
  .planner-spread { display: block; width: 1200px; height: 720px; }
  .planner-spread text { font-family: "Arvo", Georgia, serif; fill: var(--ink); }
  .page { fill: var(--paper); }
  .band { fill: var(--sage); }
  .heading { font-size: 12px; letter-spacing: 0.3px; }
  .question { font-size: 9.5px; }
  .micro { font-size: 8px; }
  .tiny { font-size: 7px; }
  .dots { stroke: var(--rule); stroke-width: 1.2; stroke-dasharray: 0.1 5.5; stroke-linecap: round; fill: none; }
  .rule { stroke: var(--grid); stroke-width: 1; fill: none; }
  .box { fill: none; stroke: var(--grid); stroke-width: 1; }
</style>
</head>
<body>
<svg class="planner-spread" viewBox="0 0 2474 1484" xmlns="http://www.w3.org/2000/svg">
  <defs>
    <g id="dot-block-7">
      <line class="dots" x1="0" y1="0" x2="386" y2="0"/>
      <line class="dots" x1="0" y1="19" x2="386" y2="19"/>
      <line class="dots" x1="0" y1="38" x2="386" y2="38"/>
      <line class="dots" x1="0" y1="57" x2="386" y2="57"/>
      <line class="dots" x1="0" y1="76" x2="386" y2="76"/>
      <line class="dots" x1="0" y1="95" x2="386" y2="95"/>
      <line class="dots" x1="0" y1="114" x2="386" y2="114"/>
      <line class="dots" x1="0" y1="133" x2="386" y2="133"/>
    </g>
    <g id="answer-block">
      <rect class="band" x="0" y="0" width="7" height="133"/>
      <line class="dots" x1="10" y1="11" x2="386" y2="11"/>
      <line class="dots" x1="10" y1="30" x2="386" y2="30"/>
      <line class="dots" x1="10" y1="49" x2="386" y2="49"/>
      <line class="dots" x1="10" y1="68" x2="386" y2="68"/>
      <line class="dots" x1="10" y1="87" x2="386" y2="87"/>
      <line class="dots" x1="10" y1="106" x2="386" y2="106"/>
      <line class="dots" x1="10" y1="125" x2="386" y2="125"/>
    </g>
    <g id="short-answer">
      <rect class="band" x="0" y="0" width="6" height="64"/>
      <line class="dots" x1="10" y1="8" x2="386" y2="8"/>
      <line class="dots" x1="10" y1="33" x2="386" y2="33"/>
      <line class="dots" x1="10" y1="58" x2="386" y2="58"/>
    </g>
    <g id="habit-grid">
      <rect class="box" x="0" y="0" width="105" height="105"/>
      <path class="rule" d="M15 0V105M30 0V105M45 0V105M60 0V105M75 0V105M90 0V105M0 15H105M0 30H105M0 45H105M0 60H105M0 75H105M0 90H105"/>
    </g>
  </defs>

  <rect width="2474" height="1484" fill="var(--canvas)"/>

  <!-- Review goals: weekly -->
  <g class="review-page" transform="translate(222,110)">
    <rect class="page" width="456" height="590"/>
    <rect class="band" x="35" y="32" width="183" height="14"/>
    <text class="heading" x="38" y="44">REVIEW GOALS</text>
    <text class="question" x="35" y="72">Did I execute what I needed to in order to move forward in my progress?</text>
    <use href="#answer-block" x="35" y="82"/>
    <text class="question" x="35" y="238">What can I take away from this week/ lessons learned?</text>
    <use href="#answer-block" x="35" y="247"/>
    <rect class="band" x="35" y="395" width="185" height="14"/>
    <text class="heading" x="37" y="406">NOTES</text>
    <use href="#dot-block-7" x="35" y="422"/>
  </g>

  <!-- Review goals: quarterly -->
  <g class="review-page" transform="translate(747,110)">
    <rect class="page" width="456" height="590"/>
    <rect class="band" x="35" y="32" width="108" height="14"/>
    <text class="heading" x="38" y="44">REVIEW GOALS</text>
    <text class="question" x="38" y="72">Did I have a meaningful impact on my life this quarter?</text>
    <use href="#answer-block" x="40" y="82"/>
    <text class="question" x="38" y="237">Did I meet my goals? Why or why not?</text>
    <use href="#answer-block" x="40" y="247"/>
    <rect class="band" x="35" y="395" width="185" height="14"/>
    <text class="heading" x="37" y="407" style="font-size:14px">NOTES</text>
    <use href="#dot-block-7" x="35" y="422"/>
  </g>

  <!-- Week page -->
  <g class="week-page" transform="translate(1272,110)">
    <rect class="page" width="456" height="590"/>
    <rect class="band" x="34" y="32" width="184" height="14"/>
    <text class="heading" x="37" y="43">WEEK</text>
    <g class="day-markers">
      <text class="tiny" x="264" y="38">MON</text><circle class="box" cx="275" cy="47" r="5"/>
      <text class="tiny" x="290" y="38">TUE</text><circle class="box" cx="300" cy="47" r="5"/>
      <text class="tiny" x="313" y="38">WED</text><circle class="box" cx="324" cy="47" r="5"/>
      <text class="tiny" x="340" y="38">THU</text><circle class="box" cx="349" cy="47" r="5"/>
      <text class="tiny" x="367" y="38">FRI</text><circle class="box" cx="373" cy="47" r="5"/>
      <text class="tiny" x="390" y="38">SAT</text><circle class="box" cx="398" cy="47" r="5"/>
      <text class="tiny" x="413" y="38">SUN</text><circle class="box" cx="422" cy="47" r="5"/>
    </g>
    <text class="question" x="38" y="75">PRIMARY TASK</text>
    <g class="primary-tasks">
      <rect class="box" x="38" y="92" width="9" height="9"/><text class="question" x="53" y="100">1</text>
      <line class="dots" x1="62" y1="96" x2="266" y2="96"/><line class="dots" x1="62" y1="114" x2="266" y2="114"/><line class="dots" x1="62" y1="132" x2="266" y2="132"/><line class="dots" x1="62" y1="150" x2="266" y2="150"/>
      <rect class="box" x="38" y="177" width="9" height="9"/><text class="question" x="53" y="185">2</text>
      <line class="dots" x1="62" y1="181" x2="266" y2="181"/><line class="dots" x1="62" y1="199" x2="266" y2="199"/><line class="dots" x1="62" y1="217" x2="266" y2="217"/><line class="dots" x1="62" y1="235" x2="266" y2="235"/>
      <rect class="box" x="38" y="263" width="9" height="9"/><text class="question" x="53" y="271">3</text>
      <line class="dots" x1="62" y1="267" x2="266" y2="267"/><line class="dots" x1="62" y1="285" x2="266" y2="285"/><line class="dots" x1="62" y1="303" x2="266" y2="303"/><line class="dots" x1="62" y1="321" x2="266" y2="321"/>
    </g>
    <text class="question" x="36" y="362">SECONDARY TASK</text>
    <g class="secondary-tasks">
      <line class="dots" x1="36" y1="380" x2="266" y2="380"/><line class="dots" x1="36" y1="398" x2="266" y2="398"/><line class="dots" x1="36" y1="416" x2="266" y2="416"/><line class="dots" x1="36" y1="434" x2="266" y2="434"/><line class="dots" x1="36" y1="452" x2="266" y2="452"/><line class="dots" x1="36" y1="470" x2="266" y2="470"/><line class="dots" x1="36" y1="488" x2="266" y2="488"/>
    </g>
    <g class="hour-schedule">
      <rect class="band" x="296" y="95" width="34" height="412"/>
      <path class="rule" d="M296 95H425M296 113H425M296 131H425M296 149H425M296 167H425M296 185H425M296 203H425M296 221H425M296 239H425M296 257H425M296 275H425M296 293H425M296 311H425M296 329H425M296 347H425M296 365H425M296 383H425M296 401H425M296 419H425M296 437H425M296 455H425M296 473H425M296 491H425M296 507H425"/>
      <text class="micro" x="299" y="108">5 AM</text>
    </g>
    <rect class="box" x="38" y="509" width="9" height="9"/><text class="question" x="53" y="518">PHYSICAL ACTIVITY</text>
    <rect class="box" x="38" y="527" width="9" height="9"/><text class="question" x="53" y="536">HABIT</text>
    <rect class="box" x="38" y="545" width="9" height="9"/><text class="question" x="53" y="554">WEEKLY CHALLENGE</text>
    <text class="question" x="294" y="554">DAILY SCORE W/L</text>
    <line class="rule" x1="390" y1="553" x2="424" y2="553"/>
  </g>

  <!-- Weekly overview -->
  <g class="overview-page" transform="translate(1798,110)">
    <rect class="page" width="456" height="590"/>
    <rect class="band" x="34" y="32" width="184" height="14"/>
    <text class="heading" x="37" y="43">WEEKLY OVERVIEW</text>
    <line class="dots" x1="34" y1="62" x2="422" y2="62"/><line class="dots" x1="34" y1="80" x2="422" y2="80"/>
    <g class="focus-areas">
      <text class="tiny" x="34" y="121">Health</text><rect class="box" x="66" y="114" width="8" height="8"/>
      <text class="tiny" x="87" y="121">Career</text><rect class="box" x="119" y="114" width="8" height="8"/>
      <text class="tiny" x="140" y="121">Intellectual</text><rect class="box" x="192" y="114" width="8" height="8"/>
      <text class="tiny" x="228" y="121">Spiritual</text><rect class="box" x="250" y="114" width="8" height="8"/>
      <text class="tiny" x="270" y="121">Relationship/family</text><rect class="box" x="354" y="114" width="8" height="8"/>
      <text class="tiny" x="376" y="121">Finacial</text><rect class="box" x="412" y="114" width="8" height="8"/>
    </g>
    <text class="question" x="34" y="150">How Will You Measure Success?</text>
    <line class="dots" x1="34" y1="165" x2="422" y2="165"/><line class="dots" x1="34" y1="183" x2="422" y2="183"/><line class="dots" x1="34" y1="201" x2="422" y2="201"/><line class="dots" x1="34" y1="219" x2="422" y2="219"/>
    <text class="question" x="34" y="245">What Are The First Actionable Steps You Can Take?</text>
    <g class="action-steps">
      <rect class="band" x="34" y="249" width="37" height="80"/>
      <path class="rule" d="M34 249H422M34 269H422M34 289H422M34 309H422M34 329H422M34 249V329M71 249V329"/>
    </g>
    <text class="question" x="34" y="350">Why Do You Want To Achieve This?</text>
    <line class="dots" x1="34" y1="366" x2="422" y2="366"/><line class="dots" x1="34" y1="384" x2="422" y2="384"/><line class="dots" x1="34" y1="402" x2="422" y2="402"/><line class="dots" x1="34" y1="420" x2="422" y2="420"/>
    <g class="habit-streak">
      <rect class="band" x="35" y="451" width="24" height="105"/>
      <rect class="box" x="35" y="451" width="24" height="105"/>
      <text class="micro" transform="translate(51,545) rotate(-90)">HABIT STREAK</text>
      <text class="question" x="101" y="447">MONTH 1</text>
      <use href="#habit-grid" x="74" y="451"/>
      <text class="question" x="223" y="447">MONTH 2</text>
      <use href="#habit-grid" x="196" y="451"/>
      <text class="question" x="342" y="447">MONTH 3</text>
      <use href="#habit-grid" x="317" y="451"/>
    </g>
  </g>

  <!-- Month page -->
  <g class="month-page" transform="translate(222,760)">
    <rect class="page" width="456" height="590"/>
    <rect class="band" x="35" y="32" width="184" height="14"/>
    <text class="heading" x="39" y="44">MONTH</text>
    <g class="month-calendar">
      <rect class="box" x="35" y="60" width="386" height="310"/>
      <path class="rule" d="M90 60V370M145 60V370M200 60V370M255 60V370M310 60V370M366 60V370M35 112H421M35 163H421M35 215H421M35 267H421M35 318H421"/>
    </g>
    <rect class="band" x="35" y="395" width="185" height="14"/>
    <text class="heading" x="37" y="406">NOTES</text>
    <use href="#dot-block-7" x="35" y="422"/>
  </g>

  <!-- Weekly review -->
  <g class="weekly-review-page" transform="translate(747,760)">
    <rect class="page" width="456" height="590"/>
    <rect class="band" x="35" y="32" width="183" height="14"/>
    <text class="heading" x="38" y="44">WEEKLY REVIEW</text>
    <text class="question" x="34" y="72">What Did I Learn This Week/ What Can I Take Away?</text>
    <use href="#short-answer" x="35" y="85"/>
    <text class="question" x="34" y="173">Did I Execute What I Needed To Move Forward In My Goals?</text>
    <use href="#short-answer" x="35" y="186"/>
    <text class="question" x="34" y="271">What Can I Improve/keep Doing For Next Week?</text>
    <use href="#short-answer" x="35" y="285"/>
    <rect class="band" x="35" y="365" width="185" height="14"/>
    <text class="heading" x="37" y="376">NOTES</text>
    <use href="#dot-block-7" x="35" y="392"/>
    <text class="question" x="34" y="552">DAILY SCORE</text>
    <g class="daily-score">
      <rect class="box" x="110" y="542" width="130" height="11"/>
      <path class="rule" d="M128.5 542V553M147 542V553M165.5 542V553M184 542V553M202.5 542V553M221 542V553"/>
    </g>
    <text class="question" x="295" y="552">WEEKLY W/L</text>
    <rect class="box" x="376" y="542" width="43" height="11"/>
  </g>

  <!-- Notes page -->
  <g class="notes-page" transform="translate(1272,760)">
    <rect class="page" width="456" height="590"/>
    <rect class="band" x="34" y="32" width="184" height="14"/>
    <text class="heading" x="37" y="44">NOTES</text>
    <use href="#dot-block-7" x="35" y="66"/>
    <use href="#dot-block-7" x="35" y="218"/>
    <use href="#dot-block-7" x="35" y="370"/>
    <line class="dots" x1="35" y1="522" x2="421" y2="522"/>
    <line class="dots" x1="35" y1="541" x2="421" y2="541"/>
    <line class="dots" x1="35" y1="556" x2="421" y2="556"/>
  </g>

  <!-- Goals page -->
  <g class="goals-page" transform="translate(1798,760)">
    <rect class="page" width="456" height="590"/>
    <rect class="band" x="34" y="32" width="184" height="14"/>
    <text class="heading" x="37" y="44">GOALS</text>
    <line class="dots" x1="34" y1="75" x2="292" y2="75"/><line class="dots" x1="34" y1="99" x2="292" y2="99"/><line class="dots" x1="34" y1="124" x2="292" y2="124"/><line class="dots" x1="34" y1="148" x2="292" y2="148"/>
    <g class="focus-areas">
      <text class="question" x="34" y="180">Health</text><rect class="box" x="75" y="171" width="8" height="8"/>
      <text class="question" x="127" y="180">Financial</text><rect class="box" x="181" y="171" width="8" height="8"/>
      <text class="question" x="233" y="180">Spiritual</text><rect class="box" x="284" y="171" width="8" height="8"/>
      <text class="question" x="34" y="204">Career</text><rect class="box" x="75" y="195" width="8" height="8"/>
      <text class="question" x="122" y="205">Family/relationship</text><rect class="box" x="226" y="197" width="8" height="8"/>
    </g>
    <rect class="band" x="34" y="222" width="184" height="14"/>
    <text class="heading" x="37" y="233">3 WEEKLY GOALS</text>
    <text class="heading" x="34" y="256">1</text>
    <line class="dots" x1="34" y1="265" x2="292" y2="265"/><line class="dots" x1="34" y1="287" x2="292" y2="287"/><line class="dots" x1="34" y1="309" x2="292" y2="309"/><line class="dots" x1="34" y1="330" x2="292" y2="330"/>
    <text class="heading" x="34" y="368">2</text>
    <line class="dots" x1="34" y1="378" x2="292" y2="378"/><line class="dots" x1="34" y1="400" x2="292" y2="400"/><line class="dots" x1="34" y1="422" x2="292" y2="422"/><line class="dots" x1="34" y1="443" x2="292" y2="443"/>
    <text class="heading" x="34" y="480">3</text>
    <line class="dots" x1="34" y1="490" x2="292" y2="490"/><line class="dots" x1="34" y1="512" x2="292" y2="512"/><line class="dots" x1="34" y1="534" x2="292" y2="534"/><line class="dots" x1="34" y1="555" x2="292" y2="555"/>
    <g class="weekday-column">
      <line class="rule" x1="314" y1="75" x2="421" y2="75"/><text class="tiny" x="314" y="85">MONDAY</text>
      <line class="rule" x1="314" y1="144" x2="421" y2="144"/><text class="tiny" x="314" y="154">TUESDAY</text>
      <line class="rule" x1="314" y1="213" x2="421" y2="213"/><text class="tiny" x="314" y="223">WEDNESDAY</text>
      <line class="rule" x1="314" y1="282" x2="421" y2="282"/><text class="tiny" x="314" y="292">THURSDAY</text>
      <line class="rule" x1="314" y1="351" x2="421" y2="351"/><text class="tiny" x="314" y="361">FRIDAY</text>
      <line class="rule" x1="314" y1="420" x2="421" y2="420"/><text class="tiny" x="314" y="430">SATURDAY</text>
      <line class="rule" x1="314" y1="489" x2="421" y2="489"/><text class="tiny" x="314" y="499">SUNDAY</text>
    </g>
  </g>
</svg>
</body>
</html>
```